Etiketten-Design für Weinflasche
Sehr gute Zusammenarbeit bei Tag und Nacht, sehr kooperativ ,flexibel und entgegenkommend. Empfehlenswert
Zielgruppe
Weinbau - Eigenbau Wein -Weinverkauf
Aufgabenstellung
Bräuchte oder Suche ein Flaschenetikette für Rotwein der Marke Zweigelt Das Ausmaß der Etikette sollte 8cm Breit und 12cm Hoch sein. Habe meine letzte Etikette beigelegt sie Anhang

```html
<!DOCTYPE html>
<html lang="de">
<head>
<meta charset="utf-8">
<title>Zweigelt 2020 – Etikettenvarianten</title>
<link rel="stylesheet" href="https://fonts.googleapis.com/css2?family=Roboto+Condensed:wght@400&family=Tinos&display=swap">
<style>
  :root {
    --page-bg: #ffffff;
    --band-dark: #333333;
    --field-mid: #3d3d3d;
    --type-faint: #5e5e5e;
    --type-light: #c9c9c9;
    --type-name: #d2d2d2;
    --accent-red: #b71c1c;
    --caption-ink: #111111;
  }
  * { box-sizing: border-box; margin: 0; padding: 0; }
  html, body {
    width: 1200px; height: 527px; overflow: hidden;
    background: var(--page-bg);
    font-family: "Roboto Condensed", "Arial Narrow", sans-serif;
  }
  .sheet { position: relative; width: 1200px; height: 527px; }

  .label {
    position: absolute; top: 0; width: 286px; height: 490px;
    background: var(--band-dark); overflow: hidden;
  }
  .label--v1 { left: 0;    --mark-y: 192px; --variety-y: 256px; }
  .label--v2 { left: 308px; --mark-y: 192px; --variety-y: 267px; }
  .label--v3 { left: 611px; --mark-y: 180px; --variety-y: 297px; }
  .label--v4 { left: 914px; --mark-y: 180px; --variety-y: 317px; }

  .label__header {
    position: absolute; top: 0; left: 0; right: 0; height: 82px;
    display: flex; align-items: center; justify-content: center;
    color: var(--type-faint); font-size: 34px; letter-spacing: 0.36em;
    padding-left: 0.36em; padding-top: 0;
  }
  .label__field {
    position: absolute; top: 82px; left: 0; right: 0; height: 328px;
    background: radial-gradient(ellipse at 50% 45%, #434343 0%, var(--field-mid) 70%, #393939 100%);
  }
  .label__footer {
    position: absolute; top: 410px; left: 0; right: 0; height: 80px;
    display: flex; align-items: center; justify-content: center;
    color: var(--type-faint); font-size: 62px; line-height: 1;
  }

  .winery-mark {
    position: absolute; left: 0; right: 0; top: var(--mark-y);
    transform: translateY(-50%);
    display: flex; flex-direction: column; align-items: center; gap: 8px;
  }
  .winery-mark__dot {
    width: 34px; height: 34px; border-radius: 50%; background: var(--accent-red);
  }
  .winery-mark__name {
    color: var(--type-name); font-size: 17px; letter-spacing: 0.04em;
  }

  .label__variety {
    position: absolute; left: 0; right: 0; top: var(--variety-y);
    text-align: center; color: var(--type-light);
    font-size: 36px; line-height: 1; letter-spacing: 0.26em; padding-left: 0.26em;
  }

  .caption {
    position: absolute; top: 500px; width: 286px; text-align: center;
    font-family: "Tinos", "Times New Roman", serif; font-size: 16px; color: var(--caption-ink);
  }
</style>
</head>
<body>
<main class="sheet">
  <section class="label label--v1">
    <div class="label__header">WEINBAU</div>
    <div class="label__field" role="img" aria-label="Dezentes Ornamentmuster aus Rankenblättern und Weintrauben"></div>
    <div class="winery-mark"><span class="winery-mark__dot"></span><span class="winery-mark__name">TOBIAS LOMANDER</span></div>
    <div class="label__variety">ZWEIGELT</div>
    <div class="label__footer">2020</div>
  </section>
  <section class="label label--v2">
    <div class="label__header">WEINBAU</div>
    <div class="label__field" role="img" aria-label="Dezentes Ornamentmuster aus Rankenblättern und Weintrauben"></div>
    <div class="winery-mark"><span class="winery-mark__dot"></span><span class="winery-mark__name">TOBIAS LOMANDER</span></div>
    <div class="label__variety">ZWEIGELT</div>
    <div class="label__footer">2020</div>
  </section>
  <section class="label label--v3">
    <div class="label__header">WEINBAU</div>
    <div class="label__field" role="img" aria-label="Dezentes Ornamentmuster aus Rankenblättern und Weintrauben"></div>
    <div class="winery-mark"><span class="winery-mark__dot"></span><span class="winery-mark__name">TOBIAS LOMANDER</span></div>
    <div class="label__variety">ZWEIGELT</div>
    <div class="label__footer">2020</div>
  </section>
  <section class="label label--v4">
    <div class="label__header">WEINBAU</div>
    <div class="label__field" role="img" aria-label="Dezentes Ornamentmuster aus Rankenblättern und Weintrauben"></div>
    <div class="winery-mark"><span class="winery-mark__dot"></span><span class="winery-mark__name">TOBIAS LOMANDER</span></div>
    <div class="label__variety">ZWEIGELT</div>
    <div class="label__footer">2020</div>
  </section>

  <div class="caption" style="left:0">1</div>
  <div class="caption" style="left:308px">2</div>
  <div class="caption" style="left:611px">3</div>
  <div class="caption" style="left:914px">4</div>
</main>
</body>
</html>
```